Bramblewick Dill Pickles needs your smart gourmet Design

Looking for a smart design for a dill pickle jar container. The text
Bramblewick Dill Pickles.
Simply Picklelicious.

A tasty reason to raid the refrigerator.

Target Market(s)

Foodies, farmers market types.

Font styles to use
Serif
Sans Serif

Colors

Designer to choose colors to be used in the design.

Requirements
Must have
• Attractive design to entice foodies to buy my Pickles. Not cluttered, easy to read.
Nice to have
• Pickles, garlic. Modern.
Should not have
• Clutter. No script text.

```html
<!DOCTYPE html>
<html lang="en">
<head>
<meta charset="utf-8">
<title>Bramblewick Dill Pickles – Jar Label</title>
<link rel="stylesheet" href="https://fonts.googleapis.com/css2?family=Comic+Neue:wght@700&family=Fredoka:wght@700&family=Jost:wght@800&display=swap">
<style>
  :root {
    --lid-orange: #e0642a;
    --lid-edge: #2d4d4f;
    --jar-dark: #4f8a32;
    --jar-light: #8cc34a;
    --jar-edge: #3b6a2a;
    --label-yellow: #ffde00;
    --label-red: #e8232e;
    --brand-green: #138a3a;
    --ink: #111111;
    --white: #ffffff;
    --art-tone: #c9d94a;
  }
  html, body {
    margin: 0;
    padding: 0;
    width: 1200px;
    height: 1200px;
    overflow: hidden;
    background: var(--white);
  }
  .canvas {
    position: relative;
    width: 1200px;
    height: 1200px;
  }
  .jar-art {
    position: absolute;
    inset: 0;
  }
  .tagline {
    position: absolute;
    left: 698px;
    top: 508px;
    margin: 0;
    font-family: "Comic Neue", "Comic Sans MS", sans-serif;
    font-weight: 700;
    font-size: 14.5px;
    line-height: 17px;
    color: var(--label-red);
  }
  .slogan-band {
    position: absolute;
    left: 505px;
    top: 763px;
    width: 207px;
    height: 27px;
    background: var(--label-red);
    color: var(--white);
    font-family: "Comic Neue", "Comic Sans MS", sans-serif;
    font-weight: 700;
    font-size: 15px;
    letter-spacing: 0.5px;
    display: flex;
    align-items: center;
    justify-content: center;
  }
  .product-name {
    position: absolute;
    left: 400px;
    top: 792px;
    width: 394px;
    margin: 0;
    text-align: center;
  }
  .brand-name {
    display: block;
    font-family: "Fredoka", "Futura", sans-serif;
    font-weight: 700;
    font-size: 48px;
    line-height: 52px;
    color: var(--brand-green);
  }
  .product-type {
    display: block;
    font-family: "Jost", "Futura", sans-serif;
    font-weight: 800;
    font-size: 46px;
    line-height: 46px;
    color: var(--ink);
  }
</style>
</head>
<body>
<main class="canvas">
  <svg class="jar-art" width="1200" height="1200" viewBox="0 0 1200 1200" xmlns="http://www.w3.org/2000/svg">
    <defs>
      <linearGradient id="jarGlass" x1="0" y1="0" x2="0" y2="1">
        <stop offset="0" stop-color="var(--jar-dark)"/>
        <stop offset="1" stop-color="var(--jar-light)"/>
      </linearGradient>
      <linearGradient id="artTone" x1="0" y1="0" x2="1" y2="1">
        <stop offset="0" stop-color="#f4d21a"/>
        <stop offset="1" stop-color="var(--art-tone)"/>
      </linearGradient>
    </defs>

    <path class="jar-body" d="M400,245 L795,245 C840,270 855,300 855,360 L855,930 Q855,1000 785,1000 L415,1000 Q345,1000 345,930 L345,360 C345,300 360,270 400,245 Z"
          fill="url(#jarGlass)" stroke="var(--jar-edge)" stroke-width="3"/>

    <g class="jar-lid">
      <rect x="385" y="135" width="423" height="113" rx="10" fill="var(--lid-orange)" stroke="var(--lid-edge)" stroke-width="3"/>
      <ellipse cx="596" cy="137" rx="211" ry="25" fill="var(--lid-orange)" stroke="var(--lid-edge)" stroke-width="3"/>
    </g>

    <path class="label-frame"
          d="M597,298 C630,335 700,340 760,335 C785,333 795,345 795,375 C795,470 820,560 820,620 C820,690 795,760 795,870 C795,900 785,910 760,908 C700,905 630,910 597,948 C564,910 494,905 434,908 C409,910 399,900 399,870 C399,760 376,690 376,620 C376,560 399,470 399,375 C399,345 409,333 434,335 C494,340 564,335 597,298 Z"
          fill="var(--label-yellow)" stroke="var(--label-red)" stroke-width="12" stroke-linejoin="round"/>

    <rect class="label-illustration" x="412" y="350" width="282" height="405" rx="18"
          fill="url(#artTone)" opacity="0.55"
          role="img" aria-label="Illustration of a cheerful cartoon pickle surrounded by garlic cloves and dill sprigs with a starburst exclamation"/>
  </svg>

  <p class="tagline">A tasty<br>reason to<br>raid the<br>refrigerator</p>

  <div class="slogan-band">SIMPLY PICKLELICIOUS!</div>

  <h1 class="product-name">
    <span class="brand-name">Bramblewick</span>
    <span class="product-type">DILL PICKLES</span>
  </h1>
</main>
</body>
</html>
```